The Brightwater Compass Business Card

We need an attractive business card with the logo that we bought from ArtVantly last year.
Our mission is to contribute to change the way today's leaders manage business companies bringing value to the workplace and helping them to build a new model of creating wealth.
Our logo is clear about our values : we seek Positive Change through People and are convinced that the pursuit of individual well-being and the chase of economic results can converge with the right management.
Management Consulting
Corinne Fabrelle
+34 612 98 70 31
corinne.fabrelle@thebrightwatercompass-mail.net
www.thebrightwatercompass-mail.net

```html
<!DOCTYPE html>
<html lang="en">
<head>
<meta charset="utf-8">
<title>The Brightwater Compass – Business Card</title>
<link rel="stylesheet" href="https://fonts.googleapis.com/css2?family=Cinzel:wght@400;500&family=Tinos&display=swap">
<style>
  :root {
    --navy: #262b3a;
    --teal: #0f7f7c;
    --white: #ffffff;
    --backdrop: #e4e5e7;
  }
  * { box-sizing: border-box; margin: 0; padding: 0; }
  html, body {
    width: 1200px; height: 1200px; overflow: hidden;
    background: var(--backdrop);
  }
  .card {
    position: absolute;
    border-radius: 22px;
    overflow: hidden;
    background: var(--white);
    box-shadow: 0 14px 30px rgba(0,0,0,0.25);
  }
  .card-front { left: 182px; top: 52px; width: 846px; height: 493px; }
  .card-back  { left: 194px; top: 607px; width: 815px; height: 489px; }
  .card-waves { position: absolute; inset: 0; width: 100%; height: 100%; }

  .brand {
    position: absolute;
    display: flex; flex-direction: column; align-items: center;
    font-family: 'Cinzel', serif; font-weight: 500;
    color: var(--teal);
    text-align: center; line-height: 1.05;
  }
  .brand-dot {
    width: 58px; height: 58px; border-radius: 50%;
    background: var(--teal); margin-bottom: 14px;
  }
  .brand-name { font-size: 36px; letter-spacing: 1px; }
  .card-front .brand { left: 420px; top: 62px; width: 360px; }
  .card-back .brand  { left: 400px; top: 52px; width: 360px; }

  .name-marker {
    position: absolute; left: 0; top: 305px; width: 22px; height: 64px;
    background: var(--navy); border-right: 5px solid var(--teal);
  }
  .person-name {
    position: absolute; left: 65px; top: 312px;
    font-family: 'Cinzel', serif; font-weight: 400;
    font-size: 46px; color: var(--teal); letter-spacing: 0.5px;
  }

  .contact-list {
    position: absolute; left: 41px; top: 308px;
    list-style: none;
  }
  .contact-item {
    display: flex; align-items: center; gap: 13px;
    height: 44px; margin-bottom: 7px;
    font-family: 'Tinos', serif; font-size: 29px; color: var(--white);
  }
  .contact-icon {
    width: 44px; height: 44px; border-radius: 50%;
    background: var(--white);
    display: flex; align-items: center; justify-content: center;
    flex: none;
  }
  .contact-icon svg { width: 26px; height: 26px; }
</style>
</head>
<body>

<section class="card card-front" aria-label="Business card front">
  <svg class="card-waves" viewBox="0 0 846 493" preserveAspectRatio="none" aria-hidden="true">
    <path fill="#0f7f7c" d="M0,0 H846 V140 C800,240 720,300 620,295 C470,285 330,40 0,100 Z"/>
    <path fill="#262b3a" d="M0,0 H846 V132 C795,232 715,288 620,282 C470,272 330,20 0,74 Z"/>
  </svg>
  <div class="brand">
    <span class="brand-dot"></span>
    <span class="brand-name">The Brightwater<br>Compass</span>
  </div>
  <span class="name-marker"></span>
  <h1 class="person-name">Corinne Fabrelle</h1>
</section>

<section class="card card-back" aria-label="Business card back">
  <svg class="card-waves" viewBox="0 0 815 489" preserveAspectRatio="none" aria-hidden="true">
    <path fill="#0f7f7c" d="M0,489 V58 C200,20 330,150 470,225 C570,278 640,295 700,270 C760,245 795,180 815,135 V489 Z"/>
    <path fill="#262b3a" d="M0,489 V84 C200,45 330,175 470,246 C570,295 645,300 705,278 C765,255 797,190 815,150 V489 Z"/>
  </svg>
  <div class="brand">
    <span class="brand-dot"></span>
    <span class="brand-name">The Brightwater<br>Compass</span>
  </div>
  <ul class="contact-list">
    <li class="contact-item">
      <span class="contact-icon">
        <svg viewBox="0 0 24 24"><path fill="#0f7f7c" d="M6.6 10.8a15.1 15.1 0 0 0 6.6 6.6l2.2-2.2c.3-.3.7-.4 1-.2 1.1.4 2.3.6 3.6.6.6 0 1 .4 1 1V20c0 .6-.4 1-1 1A17 17 0 0 1 3 4c0-.6.4-1 1-1h3.5c.6 0 1 .4 1 1 0 1.3.2 2.5.6 3.6.1.3 0 .7-.2 1z"/></svg>
      </span>
      +34 612 98 70 31
    </li>
    <li class="contact-item">
      <span class="contact-icon">
        <svg viewBox="0 0 24 24"><rect x="2.5" y="5" width="19" height="14" rx="1.5" fill="#0f7f7c"/><path d="M3 6l9 7 9-7M3 18l6.5-6M21 18l-6.5-6" fill="none" stroke="#fff" stroke-width="1.4"/></svg>
      </span>
      corinne.fabrelle@thebrightwatercompass-mail.net
    </li>
    <li class="contact-item">
      <span class="contact-icon">
        <svg viewBox="0 0 24 24" fill="none" stroke="#0f7f7c" stroke-width="1.8"><circle cx="12" cy="12" r="9"/><ellipse cx="12" cy="12" rx="4" ry="9"/><path d="M3 12h18M4.5 7.5h15M4.5 16.5h15"/></svg>
      </span>
      www.thebrightwatercompass-mail.net
    </li>
  </ul>
</section>

</body>
</html>
```